Vornel Technologies business card design

We need a business card designed with our new logo. it would be great if the card could communicate it is a technology based company.

Target Market(s)

system integrators

Industry/Entity Type

technology, IOT

Contact Information for Business Card

Name, designation, Address, telephone number, email address

Requirements
Must have
• logo and company name
Nice to have
• something to do with technology

```html
<!DOCTYPE html>
<html lang="en">
<head>
<meta charset="utf-8">
<title>Vornel Technologies – Business Card</title>
<link rel="stylesheet" href="https://fonts.googleapis.com/css2?family=Exo+2:wght@400;600;700&display=swap">
<style>
  :root {
    --backdrop: #3a3a3a;
    --card: #222222;
    --card-back: #1f1f1f;
    --orange: #f39a1c;
    --white: #f2f2f2;
    --band-grey: #e4e4e4;
    --logo-grey: #cfcfcf;
  }
  * { margin: 0; padding: 0; box-sizing: border-box; }
  html, body { width: 1200px; height: 877px; overflow: hidden; }
  body {
    background: var(--backdrop);
    font-family: "Exo 2", sans-serif;
    position: relative;
  }
  .card {
    position: absolute;
    left: 280px;
    width: 640px;
    height: 366px;
    overflow: hidden;
    box-shadow: 0 14px 30px rgba(0,0,0,.45);
  }
  .card-back { top: 52px; background: var(--card-back); }
  .card-front { top: 458px; background: var(--card); }

  .brand {
    position: absolute;
    display: flex;
    align-items: center;
    gap: 14px;
    font-weight: 700;
    text-transform: uppercase;
    letter-spacing: 2px;
    white-space: nowrap;
  }
  .brand-mark { display: block; }
  .card-back .brand {
    left: 50%; top: 50%;
    transform: translate(-50%, -50%);
    font-size: 38px;
    color: var(--logo-grey);
  }
  .card-back .brand-mark { width: 44px; height: 44px; background: var(--logo-grey); }
  .card-front .brand {
    right: 60px; top: 58px;
    font-size: 28px;
    color: var(--orange);
  }
  .card-front .brand-mark { width: 32px; height: 32px; background: var(--orange); }

  .circuit-lines { position: absolute; left: 0; top: 0; }

  .person { position: absolute; left: 56px; top: 164px; }
  .person-name {
    font-size: 30px; font-weight: 700; color: var(--orange);
    text-transform: uppercase; letter-spacing: 1px; line-height: 1;
  }
  .person-title { font-size: 17px; color: var(--white); margin-top: 4px; line-height: 1.2; }

  .contact-list { position: absolute; left: 60px; top: 266px; list-style: none; }
  .contact-list li {
    display: flex; align-items: center; gap: 10px;
    font-size: 15px; color: var(--white); line-height: 24px;
  }
  .contact-list svg { width: 13px; height: 13px; fill: var(--orange); }

  .website {
    position: absolute; right: 48px; top: 262px;
    font-size: 15px; color: var(--orange);
  }

  .band-orange {
    position: absolute; left: 0; bottom: 0;
    width: 470px; height: 12px; background: var(--orange);
  }
  .band-grey {
    position: absolute; right: 0; bottom: 0;
    width: 170px; height: 22px; background: var(--band-grey);
  }
</style>
</head>
<body>

  <section class="card card-back" aria-label="Card back">
    <div class="brand"><span class="brand-mark"></span>Vornel Technologies</div>
  </section>

  <section class="card card-front" aria-label="Card front">
    <div class="brand"><span class="brand-mark"></span>Vornel Technologies</div>

    <svg class="circuit-lines" width="640" height="366" viewBox="0 0 640 366" aria-hidden="true">
      <line x1="56" y1="236" x2="520" y2="214" stroke="#f39a1c" stroke-width="2"/>
      <circle cx="520" cy="214" r="3" fill="#f39a1c"/>
      <line x1="56" y1="244" x2="590" y2="206" stroke="#f2f2f2" stroke-width="2"/>
      <circle cx="590" cy="206" r="3" fill="#f2f2f2"/>
      <line x1="56" y1="252" x2="582" y2="216" stroke="#f39a1c" stroke-width="2"/>
      <circle cx="582" cy="216" r="3" fill="#f39a1c"/>
    </svg>

    <div class="person">
      <p class="person-name">Marcus Hale</p>
      <p class="person-title">Founder &amp; CEO</p>
    </div>

    <ul class="contact-list">
      <li>
        <svg viewBox="0 0 24 24"><path d="M6.6 10.8a15 15 0 0 0 6.6 6.6l2.2-2.2c.3-.3.7-.4 1-.2 1.1.4 2.3.6 3.6.6.6 0 1 .4 1 1V20c0 .6-.4 1-1 1A17 17 0 0 1 3 4c0-.6.4-1 1-1h3.5c.6 0 1 .4 1 1 0 1.3.2 2.5.6 3.6.1.3 0 .7-.2 1z"/></svg>
        (555) 218-4307
      </li>
      <li>
        <svg viewBox="0 0 24 24"><path d="M2 5h20v14H2zm2 2v.5l8 5 8-5V7l-8 5z"/></svg>
        marcus@vorneltechnologies.com
      </li>
    </ul>

    <p class="website">VornelTechnologies.com</p>

    <div class="band-orange"></div>
    <div class="band-grey"></div>
  </section>

</body>
</html>
```